CFO services graphic design

I own a business consulting firm called Marlowe Consulting and we need a graphic for CFO services in our colours and branding. The attached file "CFO services to be put into Marlowe consulting theme", shows the content for the design. The two other files show the theme and colours for the new design.

```html
<!DOCTYPE html>
<html lang="en">
<head>
<meta charset="UTF-8">
<title>CFO Services</title>
<link href="https://fonts.googleapis.com/css2?family=Outfit:wght@400;500;800&display=swap" rel="stylesheet">
<style>
  :root {
    --bg: #ffffff;
    --sky: #21a9e3;
    --royal: #1650ba;
    --navy: #0f3a83;
    --midnight: #0a2350;
    --orange: #f58f20;
    --ink-light: #ffffff;
    --title-shadow: #4a2a10;
  }
  html, body {
    margin: 0;
    padding: 0;
    overflow: hidden;
    background: var(--bg);
  }
  .canvas {
    position: relative;
    width: 1200px;
    height: 1200px;
    overflow: hidden;
    background: var(--bg);
    font-family: "Outfit", sans-serif;
  }
  .diagram {
    position: absolute;
    inset: 0;
  }
  .petal-sky { fill: var(--sky); }
  .petal-royal { fill: var(--royal); }
  .petal-navy { fill: var(--navy); }
  .petal-midnight { fill: var(--midnight); }
  .hub { fill: var(--orange); }

  .label {
    position: absolute;
    transform: translate(-50%, -50%);
    color: var(--ink-light);
    text-align: center;
    font-weight: 500;
    font-size: 22px;
    line-height: 22.5px;
    white-space: nowrap;
  }
  .label-detail {
    display: block;
    font-size: 17px;
    line-height: 19px;
  }
  .hub-title {
    position: absolute;
    left: 600px;
    top: 600px;
    transform: translate(-50%, -50%);
    margin: 0;
    color: var(--ink-light);
    text-align: center;
    font-weight: 800;
    font-size: 33px;
    line-height: 37px;
    letter-spacing: -0.8px;
    text-shadow: 2px 2px 0 var(--title-shadow);
    white-space: nowrap;
  }
</style>
</head>
<body>
<div class="canvas">
  <svg class="diagram" width="1200" height="1200" viewBox="0 0 1200 1200" aria-hidden="true">
    <defs>
      <mask id="cut-cost" maskUnits="userSpaceOnUse" x="0" y="0" width="1200" height="1200">
        <rect width="1200" height="1200" fill="#fff"/>
        <circle cx="387.9" cy="387.9" r="150" fill="#000"/>
        <circle cx="600" cy="600" r="225" fill="#000"/>
      </mask>
      <mask id="cut-capital" maskUnits="userSpaceOnUse" x="0" y="0" width="1200" height="1200">
        <rect width="1200" height="1200" fill="#fff"/>
        <circle cx="600" cy="300" r="150" fill="#000"/>
        <circle cx="600" cy="600" r="225" fill="#000"/>
      </mask>
      <mask id="cut-investment" maskUnits="userSpaceOnUse" x="0" y="0" width="1200" height="1200">
        <rect width="1200" height="1200" fill="#fff"/>
        <circle cx="812.1" cy="387.9" r="150" fill="#000"/>
        <circle cx="600" cy="600" r="225" fill="#000"/>
      </mask>
      <mask id="cut-performance" maskUnits="userSpaceOnUse" x="0" y="0" width="1200" height="1200">
        <rect width="1200" height="1200" fill="#fff"/>
        <circle cx="900" cy="600" r="150" fill="#000"/>
        <circle cx="600" cy="600" r="225" fill="#000"/>
      </mask>
      <mask id="cut-budgeting" maskUnits="userSpaceOnUse" x="0" y="0" width="1200" height="1200">
        <rect width="1200" height="1200" fill="#fff"/>
        <circle cx="812.1" cy="812.1" r="150" fill="#000"/>
        <circle cx="600" cy="600" r="225" fill="#000"/>
      </mask>
      <mask id="cut-risk" maskUnits="userSpaceOnUse" x="0" y="0" width="1200" height="1200">
        <rect width="1200" height="1200" fill="#fff"/>
        <circle cx="600" cy="900" r="150" fill="#000"/>
        <circle cx="600" cy="600" r="225" fill="#000"/>
      </mask>
      <mask id="cut-compliance" maskUnits="userSpaceOnUse" x="0" y="0" width="1200" height="1200">
        <rect width="1200" height="1200" fill="#fff"/>
        <circle cx="387.9" cy="812.1" r="150" fill="#000"/>
        <circle cx="600" cy="600" r="225" fill="#000"/>
      </mask>
      <mask id="cut-communication" maskUnits="userSpaceOnUse" x="0" y="0" width="1200" height="1200">
        <rect width="1200" height="1200" fill="#fff"/>
        <circle cx="300" cy="600" r="150" fill="#000"/>
        <circle cx="600" cy="600" r="225" fill="#000"/>
      </mask>
    </defs>

    <circle class="petal-sky" cx="600" cy="300" r="131" mask="url(#cut-cost)"/>
    <circle class="petal-royal" cx="812.1" cy="387.9" r="131" mask="url(#cut-capital)"/>
    <circle class="petal-navy" cx="900" cy="600" r="131" mask="url(#cut-investment)"/>
    <circle class="petal-midnight" cx="812.1" cy="812.1" r="131" mask="url(#cut-performance)"/>
    <circle class="petal-sky" cx="600" cy="900" r="131" mask="url(#cut-budgeting)"/>
    <circle class="petal-royal" cx="387.9" cy="812.1" r="131" mask="url(#cut-risk)"/>
    <circle class="petal-navy" cx="300" cy="600" r="131" mask="url(#cut-compliance)"/>
    <circle class="petal-midnight" cx="387.9" cy="387.9" r="131" mask="url(#cut-communication)"/>

    <circle class="hub" cx="600" cy="600" r="187.5"/>
  </svg>

  <h1 class="hub-title">CHIEF FINANCIAL<br>OFFICER</h1>

  <div class="label" style="left:610px; top:281px;">Cost Accounting<br>&amp; Cost<br>Management</div>
  <div class="label" style="left:830px; top:379px;">Capital<br>Structure<br>and the<br>Cost of Capital</div>
  <div class="label" style="left:918px; top:618px;">Long-term &amp;<br>Short-term<br>Investment<br>Decisions</div>
  <div class="label" style="left:816px; top:832px;">Performance<br>Evaluation</div>
  <div class="label" style="left:589px; top:920px;">Budgeting &amp;<br>Strategic<br>Planning</div>
  <div class="label" style="left:370px; top:807px;">Risk<br>Management</div>
  <div class="label" style="left:281px; top:588px;">Compliance:<br>Tax, Legal and<br>Regulatory</div>
  <div class="label" style="left:388px; top:366px;">Communication:
    <span class="label-detail">Board of Directors,<br>Creditors, Owners,<br>Investors, Credit<br>Rating Agencies</span>
  </div>
</div>
</body>
</html>
```